Are You Prepared? Know how to support your pre-natal, post-natal and family resilience

I wish to supply a manual (both hardcopy and digit/PDF file/e-booklet) to obstetricians for them to issue to expectant parents. Content will be on pre-natal, post-natal and family mental health tips. I'd like the manual to feel fresh/bright with an educational focus, not mental health stigma, in order to empower prospective parents to up skill and nurture their own resilience and that of their children. Some pages may require me to include content than others. I would also like the option of including illustrations/infographics/diagrams. Please make it compatible with Microsoft Publisher. Thank you for your efforts!!

Target Market(s)

Prospective and expectant parents, young families

Industry/Entity Type

Family Planning

Font styles to use
Serif

Colors

Designer to choose colors to be used in the design.

Requirements
Must have
• • Needed: A booklet template that I can edit content over time, add pages and manipulate the images/text boxes myself.
• • Final deliverables: title page, contents page and several [inner] page layouts that I am able to rotate. Variety in visual layouts so I may repeat combinations to form a manual of 20+ pages.
• • File formats: Microsoft Publisher preferred but PDF files can also be provided (native design files per PixelGuild standards if Publisher not used)
• © Psychologist, Mirela Kostandis
Nice to have
• Layouts similar to the ones attached
• For designers to gain context for the content, topics will include:
• - Perinatal depression - risk and protective factors
• - Birth process, plan and expectations
• - Realistic expectations to motherhood (recovery, feeding, sleep deprivation, heightened emotions, settling and unsettled baby, bonding, body image, managing priorities, partner dynamics and communication, filtering outside advice and managing family dynamics).
• - Transition of identity. Adjusting to change and fulfillment pendulum.
• Encouraging disclosure
• - Perfectionism, shame and sense of ‘maternal failure’
• - Family dynamics
• - Discipline methods, parent communication, behavioural habits
• - Partner experience - sensitivities, difficulties, support, community attitude, role expectation, bonding, relationship dynamic with partner and extended family.
• - Grandparent boundaries, assistance and transition
• - Medical professionals and perinatal mental health, evidence based info, efficiency
• - Digital screening, mental health first aid skills.
• - Travel
• - Health and special needs
• - Trauma, grief, loss. Miscarriage. Stillborn. Maternal / paternal health. Genetic issues. Fear of mobility and mortality
Should not have
• Mental illness/stigma visuals

```html
<!DOCTYPE html>
<html lang="en">
<head>
<meta charset="utf-8">
<title>Pre-natal, Post-natal and Family Mental Health Tips</title>
<link rel="stylesheet" href="https://fonts.googleapis.com/css2?family=Montserrat:wght@500;700&family=Open+Sans:wght@400;700&display=swap">
<style>
  :root {
    --backdrop: #f2f2f2;
    --page: #2b2422;
    --mint: #7fd1b0;
    --ink-light: #f4efe9;
    --ring-orange: #e9a23b;
    --ring-red: #d2472f;
    --photo-warm-a: #d9b27a;
    --photo-warm-b: #b98d67;
    --photo-warm-c: #6e5443;
  }
  * { box-sizing: border-box; margin: 0; padding: 0; }
  html, body { width: 1200px; height: 900px; overflow: hidden; background: var(--backdrop); }
  .spread {
    position: absolute; left: 200px; top: 167px;
    width: 800px; height: 566px; display: flex;
    box-shadow: 0 10px 30px rgba(0,0,0,0.18);
  }
  .page { position: relative; width: 400px; height: 566px; background: var(--page); overflow: hidden; }
  .page--inside-cover { border-right: 1px solid #221c1a; }

  .author-portrait {
    position: absolute; left: 36px; top: 215px; width: 150px; height: 115px;
    background: radial-gradient(circle at 55% 45%, var(--photo-warm-a), var(--photo-warm-b) 55%, var(--photo-warm-c));
  }
  .author-bio {
    position: absolute; left: 198px; top: 188px; width: 168px;
    font-family: "Open Sans", sans-serif; font-size: 7.4px; line-height: 10.6px;
    color: var(--ink-light); text-align: justify;
  }
  .author-bio strong { font-weight: 700; }

  .cover-title {
    position: absolute; left: 72px; top: 196px;
    font-family: "Montserrat", sans-serif; font-weight: 500;
    font-size: 17px; line-height: 20px; letter-spacing: 0.5px;
    color: var(--mint); text-transform: uppercase;
  }
  .cover-title .cover-title__accent { display: block; font-weight: 700; }
  .cover-emblem { position: absolute; left: 0; top: 0; width: 400px; height: 566px; }
</style>
</head>
<body>
  <main class="spread">
    <section class="page page--inside-cover">
      <div class="author-portrait" role="img" aria-label="Portrait photograph of psychologist Mirela Kostandis outdoors"></div>
      <p class="author-bio"><strong>Mirela Kostandis</strong> is a psychologist who is registered with the National Psychology Registry and a member of the Society of Practising Psychologists. She is an experienced school psychologist of K-12 students and consults regularly to school directors and educators on whole school well-being initiatives. Mirela also leads the clinic arm of Bright Harbour, which offers children, adults and families one-to-one and group counselling support at both Wattle Bay and Harbourside offices. Her passion for improving psychological well-being across the lifespan began during her internship when she established the Little Sprouts organisation and developed "Reach Up", an evidence based resilience program for student, parent and teacher audiences. She has appeared on Lumen TV's "The Daybreak Hour" and contributes to print and online articles. Mirela's strengths lie in her optimistic, authentic and proactive approach where she encourages clients to identify their worth and apply helpful coping strategies to increase their sense of fulfillment and well-being.</p>
    </section>

    <section class="page page--cover">
      <h1 class="cover-title">Pre-natal,<br>post-natal<br>and family mental<br>health<span class="cover-title__accent">Tips</span></h1>
      <svg class="cover-emblem" viewBox="0 0 400 566">
        <defs>
          <linearGradient id="warmField" x1="0" y1="0" x2="1" y2="1">
            <stop offset="0" stop-color="#e8c9a4"/>
            <stop offset="0.5" stop-color="#d7a86e"/>
            <stop offset="1" stop-color="#a9804f"/>
          </linearGradient>
        </defs>
        <path d="M300 272 L470 272 L470 498 L300 498 Q288 498 280 490 L230 440 Q222 432 222 420 L222 350 Q222 338 230 330 L280 280 Q288 272 300 272 Z" fill="none" stroke="var(--ring-orange)" stroke-width="1.4"/>
        <path d="M304 286 L470 286 L470 484 L304 484 Q293 484 286 477 L243 434 Q236 427 236 416 L236 354 Q236 343 243 336 L286 293 Q293 286 304 286 Z" fill="none" stroke="var(--ring-red)" stroke-width="1.4"/>
        <path d="M310 300 L470 300 L470 470 L310 470 Q300 470 293 463 L257 427 Q250 420 250 410 L250 360 Q250 350 257 343 L293 307 Q300 300 310 300 Z" fill="url(#warmField)" role="img" aria-label="Photograph of an expectant mother holding her belly in a sunlit grass field"/>
      </svg>
    </section>
  </main>
</body>
</html>
```